HARBORLINE AUTO GLASS

Mobile Glass Shop:

1) Windshield REPAIR 2)Windshield replacment 3) Rear Windshield Replacment 4) Side Window Replacment 5) car window replacment 6) Power Window Repair.

Schedual a service within 24 hour with one of our certified technicians.

See "brightvane auto repair" web site for referance on the nature of our buisness and service. www.brightvane-example.com

```html
<!DOCTYPE html>
<html lang="en">
<head>
<meta charset="utf-8">
<title>Harborline Auto Glass</title>
<link rel="stylesheet" href="https://fonts.googleapis.com/css2?family=Bebas+Neue&family=Poppins:wght@400;500;600&display=swap">
<style>
:root{
  --blue:#129ad8;
  --blue-deep:#0b6fb3;
  --blue-title:#1b82c4;
  --navy:#06263f;
  --ink:#222;
  --text:#555;
  --pale:#f3f8fc;
  --line:#cfd8df;
}
*{box-sizing:border-box;margin:0;padding:0}
html,body{width:1200px;height:4619px;overflow:hidden;background:#fff}
body{position:relative;font-family:'Poppins',sans-serif;color:var(--text)}
.abs{position:absolute}
.display{font-family:'Bebas Neue',sans-serif;font-weight:400;letter-spacing:.5px}
a{color:inherit;text-decoration:none}

/* header */
.top-line{left:0;top:0;width:1200px;height:4px;background:var(--blue)}
.appointment{left:866px;top:0;width:223px;height:50px;background:var(--blue);clip-path:polygon(14px 0,100% 0,100% 100%,0 100%);color:#fff;font-size:17px;display:flex;align-items:center;justify-content:center;padding-left:10px}
.brand{left:117px;top:38px;display:flex;align-items:center;gap:10px}
.brand-mark{width:40px;height:40px;background:var(--blue)}
.brand-name{font-family:'Bebas Neue',sans-serif;font-size:26px;line-height:1;color:var(--blue-deep);width:120px}
.nav{top:78px;left:440px;font-family:'Bebas Neue',sans-serif;font-size:15px;color:#222}
.nav a{position:absolute;white-space:nowrap}
.search{left:1071px;top:78px}

/* hero */
.hero-art{left:0;top:120px}
.hero-box{left:176px;top:350px;width:475px;height:364px;background:rgba(18,154,216,.92);clip-path:polygon(0 22px,100% 0,100% 100%,0 100%);border-radius:0 0 0 22px;padding:52px 44px 0 44px;color:#fff}
.hero-box .eyebrow{font-size:38px;line-height:1}
.hero-box h1{font-size:54px;line-height:1;margin-top:12px;white-space:nowrap}
.hero-box p{font-size:13px;line-height:22px;margin-top:20px;width:385px}
.btn-white{display:inline-block;margin-top:24px;background:#fff;color:#111;font-weight:600;font-size:13px;padding:8px 12px}
.dots{left:62px;top:480px;width:12px}
.dots span{display:block;width:7px;height:7px;border-radius:50%;background:#8fd0f0;margin:10px auto}
.dots span.on{background:var(--blue-deep)}
.dots b{position:absolute;left:-20px;top:46px;font-size:10px;color:var(--blue-deep);font-weight:500}

/* services */
.section-title{width:1200px;text-align:center;color:var(--blue-title);font-size:44px}
.card{width:310px;height:318px;background:#fff;box-shadow:0 0 10px rgba(0,0,0,.08);padding:7px}
.card .photo{width:296px;height:248px}
.card h3{font-family:'Bebas Neue',sans-serif;font-weight:400;font-size:20px;color:#222;margin:24px 0 0 16px}
.card.feature{background:var(--blue-deep);color:#fff;text-align:center;padding:80px 30px 0}
.card.feature h3{color:#fff;margin:0;font-size:21px}
.card.feature p{font-size:11px;line-height:19px;margin-top:10px}
.card.feature .go{margin:12px auto 0;width:22px;height:22px;border-radius:50%;background:#fff;color:var(--blue-deep);display:flex;align-items:center;justify-content:center}

/* about */
.about-bg{left:0;top:1870px;width:1200px;height:767px;background:linear-gradient(#f5f9fc,#eef5fb)}
.about-title{left:113px;top:2012px;font-size:42px;color:var(--blue-title)}
.about-copy{left:113px;top:2082px;width:470px;font-size:13px;line-height:24px;color:#555}
.about-copy p+p{margin-top:24px}
.about-media{left:640px;top:1975px;width:446px;height:520px;background:linear-gradient(135deg,#1a8fd6,#4aaee6 60%,#0b6fb3)}
.btn-blue{display:inline-block;background:var(--blue);color:#fff;font-weight:600;font-size:13px;padding:9px 18px;border-radius:3px}
.about-btn{left:113px;top:2483px}

/* testimonials */
.testi-title{left:0;top:2798px;width:1090px;text-align:center;color:#fff;font-size:44px}
.quote{width:436px;height:183px;border:1.5px solid rgba(255,255,255,.85);border-radius:0 40px 0 40px;padding:20px;display:flex;gap:20px;color:#fff}
.quote .avatar{flex:none;width:126px;height:126px;border-radius:50%;border:3px solid #fff;background:linear-gradient(135deg,#c98e6b,#4e6a52);position:relative}
.quote .avatar i{position:absolute;left:49px;bottom:-14px;width:28px;height:28px;border-radius:50%;background:#fff;color:var(--blue-deep);font-style:normal;font-weight:600;font-size:20px;line-height:32px;text-align:center}
.quote p{font-size:10px;line-height:18px;margin-top:14px}
.quote strong{display:block;font-size:14px;font-weight:600;margin-top:14px}
.arrow{width:26px;height:26px;border-radius:50%;background:#fff;color:var(--blue-deep);display:flex;align-items:center;justify-content:center}

/* contact */
.contact-bg{left:0;top:3331px;width:1200px;height:700px;background:linear-gradient(180deg,#f4f8fb 0%,#e3ecf3 60%,#dfe8ef 100%)}
.field{background:rgba(255,255,255,.55);border:1px solid var(--line);font-size:13px;color:#666;padding:0 34px;display:flex;align-items:center}
.field.msg{align-items:flex-start;padding-top:20px}
.submit{left:535px;top:3807px;width:131px;height:36px;background:var(--blue);color:#fff;font-weight:600;font-size:13px;display:flex;align-items:center;justify-content:center}

/* footer */
.footer{left:0;top:3941px;width:1200px;height:678px;background:var(--navy);border-radius:130px 130px 0 0;color:#fff}
.mail-title{left:0;top:4030px;width:1200px;text-align:center;font-size:58px;color:#fff}
.mail-form{left:274px;top:4126px;width:652px;height:50px;background:#fff;border:2px solid var(--blue);display:flex}
.mail-form span{flex:1;font-size:14px;color:#444;display:flex;align-items:center;padding-left:26px}
.mail-form b{width:137px;background:var(--blue);color:#fff;font-weight:600;font-size:16px;display:flex;align-items:center;justify-content:center}
.rule{left:113px;width:976px;height:1px;background:rgba(255,255,255,.35)}
.foot-brand{left:134px;top:4340px;display:flex;align-items:center;gap:14px}
.foot-brand .mark{width:60px;height:60px;background:var(--blue)}
.foot-brand .name{font-family:'Bebas Neue',sans-serif;font-size:40px;line-height:1;color:var(--blue);width:180px}
.col h4{font-family:'Bebas Neue',sans-serif;font-weight:400;font-size:24px;color:#fff}
.col ul{list-style:none;margin-top:18px;padding-left:14px}
.col li{font-size:13px;height:36px;color:#fff}
.loc li{display:flex;gap:14px;font-size:13px;line-height:19px;margin-bottom:18px;color:#fff}
.copyright{left:0;top:4568px;width:1200px;text-align:center;font-size:13px;color:#fff}
</style>
</head>
<body>

<header>
  <div class="abs top-line"></div>
  <a class="abs appointment display" href="#">Make an appointment</a>
  <div class="abs brand">
    <span class="brand-mark"></span>
    <span class="brand-name">Harborline Auto Glass</span>
  </div>
  <nav class="abs nav">
    <a style="left:0">Home</a>
    <a style="left:78px">About us</a>
    <a style="left:174px">Our services</a>
    <a style="left:290px">Latest blog</a>
    <a style="left:401px">Testimonials</a>
    <a style="left:519px">Contact us</a>
  </nav>
  <svg class="abs search" width="18" height="18" viewBox="0 0 18 18"><circle cx="7.5" cy="7.5" r="5.5" fill="none" stroke="#222" stroke-width="2"/><path d="M11.5 11.5 16 16" stroke="#222" stroke-width="2"/></svg>
</header>

<section class="hero">
  <svg class="abs hero-art" width="1200" height="820" viewBox="0 120 1200 820" role="img" aria-label="Photo of the rear window and tail light of a dark car on a tree-lined street">
    <defs>
      <linearGradient id="heroFill" x1="0" y1="0" x2="1" y2="1">
        <stop offset="0" stop-color="#7c8a4a"/>
        <stop offset=".45" stop-color="#44523c"/>
        <stop offset=".75" stop-color="#2a2e33"/>
        <stop offset="1" stop-color="#9aa0a6"/>
      </linearGradient>
    </defs>
    <path d="M1200 131 L260 214 C170 222 113 270 113 360 L113 740 C113 810 150 850 230 860 L1200 936 Z" fill="url(#heroFill)"/>
  </svg>
  <div class="abs dots">
    <span></span><span></span><span class="on"></span><span></span><span></span>
    <b>03</b>
  </div>
  <div class="abs hero-box">
    <div class="eyebrow display">Welcome to</div>
    <h1 class="display">Harborline Auto Glass</h1>
    <p>Lorem ipsum dolor sit amet, consectetur adipiscing elit, sed do eiusmod tempor incididunt ut labore et dolore magna aliqua. Quis ipsum</p>
    <a class="btn-white" href="#">GET STARTED</a>
  </div>
</section>

<section class="services">
  <h2 class="abs section-title display" style="top:1000px">Our latest services</h2>
  <div class="abs card" style="left:113px;top:1100px">
    <div class="photo" role="img" aria-label="Cracked windshield with sunlight" style="background:linear-gradient(135deg,#c14a3c,#5b8fcc 45%,#2c5d9e)"></div>
    <h3>Windshield repair</h3>
  </div>
  <div class="abs card" style="left:445px;top:1100px">
    <div class="photo" role="img" aria-label="Technicians fitting a new windshield" style="background:linear-gradient(135deg,#cfd6dc,#3b4750 60%,#1b2228)"></div>
    <h3>Windshield replacment</h3>
  </div>
  <div class="abs card" style="left:777px;top:1100px">
    <div class="photo" role="img" aria-label="Hands installing a rear car window" style="background:linear-gradient(135deg,#6c7680,#22272c 60%,#3a4047)"></div>
    <h3>Rear windshield replacment</h3>
  </div>
  <div class="abs card" style="left:113px;top:1444px">
    <div class="photo" role="img" aria-label="Side mirror and door of a dark car" style="background:linear-gradient(135deg,#8fb7d6,#1f2f42 55%,#0d1621)"></div>
    <h3>Side window replacment</h3>
  </div>
  <div class="abs card feature" style="left:445px;top:1444px">
    <h3>Car window replacment</h3>
    <p>Lorem ipsum dolor sit amet, consectetur adipiscing elit, sed do eiusmod tempor incididunt ut labore et dolore magna aliqua.</p>
    <div class="go"><svg width="12" height="12" viewBox="0 0 12 12"><path d="M2 6h8M6 2l4 4-4 4" stroke="currentColor" stroke-width="2" fill="none"/></svg></div>
  </div>
  <div class="abs card" style="left:777px;top:1444px">
    <div class="photo" role="img" aria-label="Side mirror of a red car" style="background:linear-gradient(135deg,#e6e6e6,#b3262b 55%,#6d1418)"></div>
    <h3>Windshield repair</h3>
  </div>
</section>

<section class="about">
  <div class="abs about-bg"></div>
  <h2 class="abs about-title display">About Harborline Auto Glass</h2>
  <div class="abs about-copy">
    <p>Lorem ipsum dolor sit amet, consectetur adipiscing elit, sed do eiusmod tempor incididunt ut labore et dolore magna aliqua. Quis ipsum suspendisse ultrices gravida. Risus commodo viverra maecenas accumsan lacus vel facilisis.</p>
    <p>Contrary to popular belief, Lorem Ipsum is not simply random text. It has roots in a piece of classical Latin literature from 45 BC, making it over 2000 years old. Daniel Ashworth, a Latin professor at Marlow Hill College, looked up one of the more obscure Latin words, consectetur, from a Lorem Ipsum passage, and going through the cites of the word in classical literature, discovered the undoubtable source. Lorem Ipsum comes from sections 1.10.32 and 1.10.33 of "de Finibus Bonorum et Malorum" (The Extremes of Good and Evil) by Marcus Vell, written in 45 BC. This book is a treatise on the theory of ethics,</p>
  </div>
  <a class="abs btn-blue about-btn" href="#">READ MORE</a>
  <div class="abs about-media" role="img" aria-label="Illustration of a sheet of blue auto glass with an impact crack"></div>
</section>

<section class="testimonials">
  <svg class="abs" style="left:0;top:2630px" width="1200" height="710" viewBox="0 2630 1200 710" role="img" aria-label="Blue-tinted photo of a technician working on a windshield">
    <defs>
      <linearGradient id="bandFill" x1="0" y1="0" x2="1" y2="1">
        <stop offset="0" stop-color="#0a6fb6"/>
        <stop offset="1" stop-color="#075c9c"/>
      </linearGradient>
    </defs>
    <path d="M0 2637 L985 2713 C1050 2718 1087 2760 1087 2830 L1087 3130 C1087 3210 1040 3240 960 3255 L0 3331 Z" fill="url(#bandFill)"/>
  </svg>
  <h2 class="abs testi-title display">Our happy customers</h2>
  <div class="abs quote" style="left:113px;top:2906px">
    <div class="avatar" role="img" aria-label="Portrait of a smiling customer"><i>“</i></div>
    <div>
      <p>Lorem ipsum dolor sit amet, consectetur adipiscing elit, sed do eiusmod tempor incididunt ut labore et dolore magna aliqua. Quis ipsum suspendisse ultrices gravida.</p>
      <strong>Mara Ellison</strong>
    </div>
  </div>
  <div class="abs quote" style="left:588px;top:2906px">
    <div class="avatar" role="img" aria-label="Portrait of a smiling customer"><i>“</i></div>
    <div>
      <p>Lorem ipsum dolor sit amet, consectetur adipiscing elit, sed do eiusmod tempor incididunt ut labore et dolore magna aliqua. Quis ipsum suspendisse ultrices gravida.</p>
      <strong>Mara Ellison</strong>
    </div>
  </div>
  <div class="abs arrow" style="left:537px;top:3132px"><svg width="12" height="12" viewBox="0 0 12 12"><path d="M10 6H2M6 2 2 6l4 4" stroke="currentColor" stroke-width="2" fill="none"/></svg></div>
  <div class="abs arrow" style="left:574px;top:3132px"><svg width="12" height="12" viewBox="0 0 12 12"><path d="M2 6h8M6 2l4 4-4 4" stroke="currentColor" stroke-width="2" fill="none"/></svg></div>
</section>

<section class="contact">
  <div class="abs contact-bg" role="img" aria-label="Faded photo of a technician fitting a windshield"></div>
  <h2 class="abs section-title display" style="top:3400px">Get in touch with us</h2>
  <div class="abs field" style="left:144px;top:3486px;width:439px;height:59px">First Name</div>
  <div class="abs field" style="left:617px;top:3486px;width:438px;height:59px">Last Name</div>
  <div class="abs field" style="left:144px;top:3563px;width:439px;height:57px">Email Address</div>
  <div class="abs field" style="left:617px;top:3563px;width:438px;height:57px">Phone Number</div>
  <div class="abs field msg" style="left:144px;top:3638px;width:911px;height:108px">Message Here....</div>
  <a class="abs submit" href="#">SUBMIT NOW</a>
</section>

<footer>
  <div class="abs footer"></div>
  <h2 class="abs mail-title display">Join our mailing list</h2>
  <div class="abs mail-form"><span>Enter Your Email Address</span><b>Get Started</b></div>
  <div class="abs rule" style="top:4225px"></div>
  <div class="abs foot-brand">
    <span class="mark"></span>
    <span class="name">Harborline Auto Glass</span>
  </div>
  <div class="abs col" style="left:449px;top:4288px">
    <h4>Quick links</h4>
    <ul><li>Home</li><li>About Us</li><li>Our Services</li><li>Reviews</li></ul>
  </div>
  <div class="abs col" style="left:621px;top:4288px">
    <h4>Legal links</h4>
    <ul><li>Privacy Policy</li><li>Terms &amp; Conditions</li><li>Login / Sign up</li><li>Contact Us</li></ul>
  </div>
  <div class="abs col" style="left:841px;top:4288px">
    <h4>Location</h4>
    <ul class="loc" style="padding-left:3px;margin-top:20px">
      <li><svg width="14" height="18" viewBox="0 0 14 18"><path d="M7 1a6 6 0 0 0-6 6c0 4.5 6 10 6 10s6-5.5 6-10a6 6 0 0 0-6-6z" fill="#129ad8"/><circle cx="7" cy="7" r="2.2" fill="#06263f"/></svg><span>48 Quayside Road,<br>Port Elwin, ME 04190</span></li>
      <li><svg width="14" height="16" viewBox="0 0 16 16"><path d="M3 1l3 0 1.5 4-2 1.5a9 9 0 0 0 4 4L11 8.5l4 1.5v3a2 2 0 0 1-2 2A12 12 0 0 1 1 3a2 2 0 0 1 2-2z" fill="#129ad8"/></svg><span>555-014-2290</span></li>
      <li><svg width="16" height="14" viewBox="0 0 16 12"><rect x="0" y="0" width="16" height="12" rx="1.5" fill="#129ad8"/><path d="M1 1l7 6 7-6" stroke="#06263f" stroke-width="1.5" fill="none"/></svg><span>hello@harborlineglass.example</span></li>
    </ul>
  </div>
  <div class="abs rule" style="top:4535px"></div>
  <div class="abs copyright">©2022 Harborline Auto Glass | All Rights Reserved.</div>
</footer>

</body>
</html>
```